Events publishing website

Have increased the budget for Coded website design. Thanks
-
We need a wordpress website for events publishing. The website will be using all different kinds of events (social, business, music etc). The website should allow user to submit the new events. the new events will be published after admin reviewed.
Key menu items & requirements
- New Events (1-show picture, short description & start/end date. User can view more details in another page. 2-have categories, such as locations, free/ticked, event type etc. 3 - allow user to share the events in social website)
- Event organizer list (show the full list and most popular event organizers. users can view the list by categories, similar to above)
- events establishments (allow user to publish events related informations such as equipments, venue informations etc)
- discussion forum
Key functions
-registration page (new users should fill name, location, normal users or event organizer, types of event organizer etc)
-allow user to change locations to view different events
-search function
The functions should be similar to the following, the design should not. The website should not look like a proper website.
http://www.plumgatherhub.net
Reason: Hi All, have extended few days to allow some changes to be made for current design. Thanks
Events

```html
<!DOCTYPE html>
<html lang="en">
<head>
<meta charset="utf-8">
<title>Events</title>
<link href="https://fonts.googleapis.com/css2?family=Signika:wght@300;400&family=Open+Sans:wght@400;600&display=swap" rel="stylesheet">
<style>
:root{
  --teal:#3f7a70;
  --teal-dark:#2f5f57;
  --ink:#222;
  --muted:#555;
  --panel:#ffffff;
  --orange:#f29a1d;
  --share:#3b8fd1;
}
*{box-sizing:border-box;margin:0;padding:0}
html,body{width:1200px;height:2699px;overflow:hidden}
body{font-family:"Open Sans",sans-serif;color:var(--ink);background:radial-gradient(ellipse at 18% 10%,#fbfaf6 0,#efece5 40%,#e6e2d9 100%);position:relative}
.topbar{height:36px;background:#111;color:#fff;font-size:12px;display:flex;align-items:center;padding-left:34px;gap:10px;letter-spacing:.3px}
.topbar .sep{color:#888}
.brand{position:absolute;left:44px;top:72px;font-family:"Signika",sans-serif;color:var(--teal)}
.brand h1{font-weight:300;font-size:44px;line-height:1}
.brand p{font-weight:300;font-size:18px;margin-top:4px}
.account{position:absolute;right:28px;top:64px;display:flex;gap:22px;font-family:"Signika",sans-serif;font-weight:300;font-size:17px;color:var(--teal-dark)}
.account span{display:flex;align-items:center;gap:6px}
.search{position:absolute;left:834px;top:110px;display:flex}
.search input{width:302px;height:40px;border:1px solid #ccc;padding:0 12px;font-size:14px;font-family:inherit;color:#777}
.search button{width:40px;height:40px;border:0;background:var(--orange);color:#fff;font-size:15px;font-family:"Signika",sans-serif}
.nav{position:absolute;left:34px;top:171px;width:1146px;height:67px;background:linear-gradient(#4e8a80,#356b62);display:flex;border:1px solid #2b5a52}
.nav a{color:#fff;text-decoration:none;font-family:"Signika",sans-serif;font-weight:300;font-size:21px;padding:0 34px;display:flex;align-items:center;border-right:1px solid #2c5a53;box-shadow:1px 0 0 #5f998f}
.banner{position:absolute;left:34px;top:238px;width:1146px;height:356px;background:linear-gradient(90deg,#2c3a55 0%,#5d6f8c 25%,#3a2b26 55%,#a9431c 78%,#3b1b12 100%)}
.arrow{position:absolute;top:378px;width:38px;height:48px;background:#eee;border-radius:24px;display:flex;align-items:center;justify-content:center;color:#888;font-size:26px}
.arrow.l{left:28px}.arrow.r{right:16px}
.main{position:absolute;left:34px;top:594px;width:804px;height:1719px;background:var(--panel);border:1px solid #ddd}
.filter{margin:12px 10px 0;height:52px;background:#222;display:flex;align-items:center;padding:0 16px;gap:8px;color:#fff;font-family:"Signika",sans-serif;font-weight:300;font-size:19px;white-space:nowrap}
.filter i{display:inline-block;width:140px;height:20px;background:#fff;border-radius:10px;margin-right:12px}
.filter b{margin-left:auto;background:#000;border:1px solid #555;padding:3px 10px;font-weight:300;font-size:18px}
.total{font-family:"Signika",sans-serif;font-weight:300;font-size:19px;margin:22px 0 0 28px}
.event{position:relative;height:236px;margin:0 24px;border-bottom:1px dashed #9ab}
.event.last{border:0}
.thumb{position:absolute;left:4px;top:24px;width:241px;height:178px;border:5px solid #fff;box-shadow:0 0 4px #999}
.event .body{position:absolute;left:290px;top:26px;width:460px}
.event h2{font-family:"Signika",sans-serif;font-weight:300;font-size:20px}
.event p{font-size:12.5px;line-height:19px;margin-top:4px}
.event .meta{font-size:12.5px;margin-top:9px}
.share{display:flex;align-items:center;gap:8px;font-size:12.5px;margin-top:10px}
.share i{width:26px;height:26px;background:var(--share);border-radius:3px}
.pager{position:absolute;right:20px;bottom:30px;font-family:"Signika",sans-serif;font-weight:300;font-size:17px;display:flex;gap:10px;align-items:center}
.pager .on{width:24px;height:24px;border-radius:12px;background:var(--teal);color:#fff;display:flex;align-items:center;justify-content:center}
.pager-line{position:absolute;left:24px;right:20px;bottom:70px;border-top:1px solid #ddd}
.side{position:absolute;left:846px;top:594px;width:326px;height:1719px;background:var(--panel);border:1px solid #ddd}
.side h3{height:50px;background:linear-gradient(#fff,#e7ece9);font-family:"Signika",sans-serif;font-weight:300;font-size:22px;color:var(--teal-dark);padding:13px 0 0 16px;margin-top:12px}
.box{padding:14px 16px 10px;height:348px}
.box.rel{height:356px;padding-top:8px}
.box.org-text{height:auto;padding-top:6px}
.box .pic{height:122px;border:4px solid #fff;box-shadow:0 0 4px #888}
.box h4{font-family:"Signika",sans-serif;font-weight:300;color:var(--teal);font-size:18px;margin-top:14px}
.box .when{font-size:12px;margin-top:2px}
.box p{font-size:12.5px;line-height:20px;color:var(--muted);margin-top:6px;padding-right:10px}
.more{display:block;color:var(--teal);font-size:13px;margin-top:8px}
.edit{text-align:right;font-size:12px;color:var(--muted);padding:6px 16px 0;height:24px}
.org{display:flex;gap:14px;padding:14px 16px 0}
.org .face{width:92px;height:92px;flex:none;background:linear-gradient(#c9b9a3,#8f7a66)}
.org small{font-size:12.5px;color:var(--muted);line-height:20px}
.org strong{display:block;font-family:"Signika",sans-serif;font-weight:300;font-size:17px;margin:4px 0}
.sort{margin:40px 20px 0;height:40px;border:1px solid #bbb;border-radius:6px;font-size:12px;color:var(--muted);display:flex;align-items:center;padding:0 14px 0 38px;justify-content:space-between}
.post{margin:54px 20px 0;height:42px;background:linear-gradient(#4f897f,#2f5f57);color:#fff;font-family:"Signika",sans-serif;font-weight:300;font-size:21px;text-align:center;line-height:42px;border-radius:5px}
.footer{position:absolute;left:34px;top:2329px;width:1146px;height:370px;background:linear-gradient(#5b9286,#3d6f67 60%,#2f5b54)}
.footer h5{position:absolute;top:28px;font-family:"Signika",sans-serif;font-weight:300;font-size:21px;color:#fff}
.links{position:absolute;left:50px;top:70px;display:grid;grid-template-columns:165px 165px 165px 190px;width:685px}
.links span{font-size:13.5px;color:#fff;height:33px;line-height:33px;border-bottom:1px solid #6f9d94;padding-left:6px}
.circles{position:absolute;left:766px;top:74px;display:flex;gap:8px}
.circles i{width:30px;height:30px;border-radius:15px;background:#fff}
.copy{position:absolute;left:14px;right:14px;top:246px;height:56px;background:rgba(0,0,0,.12);color:#fff;font-size:11.5px;padding:20px 32px}
</style>
</head>
<body>
<div class="topbar"><span>EVENTS</span><span class="sep">|</span><span>NEWS EVENTS</span><span class="sep">|</span><span>SAVOUR</span><span class="sep">|</span><span>EVENT INTERNATIONAL ART SERIES</span><span class="sep">|</span><span>PLUM GATHER CALENDAR</span></div>

<div class="brand"><h1>Events</h1><p>your company slogan here</p></div>
<div class="account">
  <span><svg width="18" height="18" viewBox="0 0 18 18"><path d="M2 8h3v9H2zM6 8l4-7c2 0 2 2 1 5h5l-1 11H6z" fill="#2f5f57"/></svg>SIGN UP</span>
  <span><svg width="18" height="20" viewBox="0 0 18 20"><rect x="2" y="9" width="14" height="11" fill="#2f5f57"/><path d="M5 9V6a4 4 0 018 0v3" stroke="#2f5f57" stroke-width="2.4" fill="none"/></svg>LOGIN</span>
  <span><svg width="22" height="22" viewBox="0 0 22 22"><circle cx="11" cy="6" r="5" fill="#2f5f57"/><path d="M1 22c0-7 20-7 20 0z" fill="#2f5f57"/></svg>MEMBER</span>
</div>
<div class="search"><input value="Enter Keyword here"><button>Go</button></div>

<nav class="nav"><a>MAIN</a><a>POPULAR</a><a>EVENT ORGANIZER</a><a>FORUM</a><a>HELP</a><a>CONTACT US</a></nav>
<div class="banner" role="img" aria-label="Conference hall with stage screens and rows of seats"></div>
<div class="arrow l">‹</div><div class="arrow r">›</div>

<main class="main">
  <div class="filter">Date: <i></i>Category: <i></i>Location: <i></i><b>GO ›</b></div>
  <div class="total">Total Events 30</div>

  <article class="event"><div class="thumb" role="img" aria-label="Treasure hunt winner holding prize money" style="background:linear-gradient(#1d2238,#6b6a60)"></div>
    <div class="body"><h2>Sydney Treasure Hunt on the Monorail</h2><p>E-Commerce is a major progress in technology that has changed the way in which the customers now purchase information, products and the services. I</p><div class="meta">20 March 2012 &nbsp;until &nbsp;20 April 2012</div><div class="meta">Any Monorail Station</div><div class="meta">Chicago, IL</div><div class="share">Share With <i></i><i></i><i></i></div></div></article>

  <article class="event"><div class="thumb" role="img" aria-label="Laser light show at a music event" style="background:linear-gradient(#0c2a2e,#2d8a7c)"></div>
    <div class="body"><h2>18th Harbourside Art Showcase</h2><p>E-Commerce is a major progress in technology that has changed the way in which the customers now purchase information, products and the services. I</p><div class="meta">20 March 2012 &nbsp;until &nbsp;20 April 2012</div><div class="meta">Any Monorail Station</div><div class="meta">Chicago, IL</div><div class="share">Share With <i></i><i></i><i></i></div></div></article>

  <article class="event"><div class="thumb" role="img" aria-label="Award ceremony on a lit stage" style="background:linear-gradient(#2a2350,#7a3a6a)"></div>
    <div class="body"><h2>The Permanent Exhibition</h2><p>E-Commerce is a major progress in technology that has changed the way in which the customers now purchase information, products and the services. I</p><div class="meta">20 March 2012 &nbsp;until &nbsp;20 April 2012</div><div class="meta">Any Monorail Station</div><div class="meta">Chicago, IL</div><div class="share">Share With <i></i><i></i><i></i></div></div></article>

  <article class="event"><div class="thumb" role="img" aria-label="Gala dinner hall with purple lighting" style="background:linear-gradient(#3a1f4e,#b04aa0)"></div>
    <div class="body"><h2>Convict NewYork Exhibition</h2><p>E-Commerce is a major progress in technology that has changed the way in which the customers now purchase information, products and the services. I</p><div class="meta">20 March 2012 &nbsp;until &nbsp;20 April 2012</div><div class="meta">Any Monorail Station</div><div class="meta">Chicago, IL</div><div class="share">Share With <i></i><i></i><i></i></div></div></article>

  <article class="event"><div class="thumb" role="img" aria-label="Banquet tables set under violet light" style="background:linear-gradient(#4a3e9a,#cfc8e8)"></div>
    <div class="body"><h2>Sydney Treasure Hunt on the Monorail</h2><p>E-Commerce is a major progress in technology that has changed the way in which the customers now purchase information, products and the services. I</p><div class="meta">20 March 2012 &nbsp;until &nbsp;20 April 2012</div><div class="meta">Any Monorail Station</div><div class="meta">Chicago, IL</div><div class="share">Share With <i></i><i></i><i></i></div></div></article>

  <article class="event last"><div class="thumb" role="img" aria-label="Gala dinner hall with purple lighting" style="background:linear-gradient(#3a1f4e,#b04aa0)"></div>
    <div class="body"><h2>Convict NewYork Exhibition</h2><p>E-Commerce is a major progress in technology that has changed the way in which the customers now purchase information, products and the services. I</p><div class="meta">20 March 2012 &nbsp;until &nbsp;20 April 2012</div><div class="meta">Any Monorail Station</div><div class="meta">Chicago, IL</div><div class="share">Share With <i></i><i></i><i></i></div></div></article>

  <div class="pager-line"></div>
  <div class="pager"><span class="on">1</span><span>2</span><span>3</span><span>4</span><span>5</span><span>6</span><span>7</span><span>8</span><span>&nbsp;Next</span></div>
</main>

<aside class="side">
  <h3>New Events</h3>
  <div class="box"><div class="pic" role="img" aria-label="Event stage with purple lighting" style="background:linear-gradient(#2b2060,#b04aa0)"></div>
    <h4>Event Name here</h4><div class="when">10 July to 20 Aug &nbsp;| &nbsp;Sydney NW</div><p>Brightfield Studio is specialized in handling advanced web projects and the ongoing projects that require permanent maintenance and support .</p><span class="more">learn more about this event ›</span></div>
  <h3>Popular Events</h3>
  <div class="box"><div class="pic" role="img" aria-label="Prize winner at a gaming event" style="background:linear-gradient(#1f2f8a,#d9a06a)"></div>
    <h4>Event Name here</h4><div class="when">10 July to 20 Aug &nbsp;| &nbsp;Sydney NW</div><p>Brightfield Studio is specialized in handling advanced web projects and the ongoing projects that require permanent maintenance and support .</p><span class="more">learn more about this event ›</span></div>
  <h3>Related Events</h3>
  <div class="edit">Edit &nbsp;| &nbsp;View</div>
  <div class="box rel"><div class="pic" role="img" aria-label="Venue decorated with large glowing spheres" style="background:linear-gradient(#1c2f6e,#8fb0e8)"></div>
    <h4>Event Name here</h4><div class="when">10 July to 20 Aug &nbsp;| &nbsp;Sydney NW</div><p>Brightfield Studio is specialized in handling advanced web projects and the ongoing projects that require permanent maintenance and support .</p><span class="more">learn more about this event ›</span></div>
  <h3>Event Organizer</h3>
  <div class="org"><div class="face" role="img" aria-label="Organizer portrait"></div><div><small>The best best practices?</small><strong>Marlowe's</strong><small>Posted by marlowe on July 6, 2012 at 10:35am</small></div></div>
  <div class="box org-text"><p>Brightfield Studio is specialized in handling advanced web projects and the ongoing projects that require permanent maintenance and support .</p></div>
  <div class="sort">Sort By : <span>▾</span></div>
  <div class="post">POST AN EVENT</div>
</aside>

<footer class="footer">
  <h5 style="left:50px">Quick Links</h5>
  <div class="links">
    <span>Hom page</span><span>Login</span><span>Support</span><span>Term &amp; Conditions of Use</span>
    <span>Events</span><span>FAQ</span><span>Add Events</span><span>Privacy Policy</span>
    <span>Popular</span><span>Login</span><span>Speical Events</span><span>Help</span>
    <span>News</span><span>Forgot Password</span><span>Contact info</span><span></span>
  </div>
  <h5 style="left:766px">Connect with Us</h5>
  <div class="circles"><i></i><i></i><i></i></div>
  <div class="copy">© 2012 Company Name &nbsp;| &nbsp;All right reserved &nbsp;| &nbsp;Policy Privacy</div>
</footer>
</body>
</html>
```